Event Poster - Tarona Mist Fest 2018 (Need ASAP)

Create a poster for an upcoming vape event, located in Waikato, Hamilton, New Zealand.

Mist Fest is an event where lots of shops come to a location, and the public are welcomed and they all vape, buy vape products, socialize, drink beer and have fun.

VISIT THE EVENT WEBSITE FOR INFO - www.taronamistfest.co.nz

We have created a website at, as you can see the logo and design is a bit boring and plain, so we dont really want it to look anything like that, The logo that is created to suit the poster will be able to be

Need a poster done up so we can send it around, post it up on boards, share on social media etc

I have attached previous events from nearby towns, for reference, but I want something much better.

Target Market(s)

25-45 Male / Female

Requirements
Must have
• - Tarona Mist Fest 2018
• - Saturday, 2nd June 2018
• - 12-10pm
• - R18 Event (important for public to know)
• - Vendors, Prizes, Comps, E Juice Awards, Entertainment, Giveaways & More
• - The Corner Alehouse (52 Mulgrave Rd, Kerepuni, Hamilton)
• - mention something along lines "Come To Tarona's First Mist Fest"
• - "Get Your Tickets from www.taronamistfest.co.nz TODAY"
• - I want people to know they can buy it from a store as well "The Cloud Barn"
Nice to have
• Our City colors are Red,Yellow,Black which is symbolic for "Waikato" so it would be nice to have those integrated in there. Alot of the other Mist Fest events have dark, bogan, amateur look done to them, so I want ours to be just a much better version.
• To Clarify, Hamilton is a city inside the Waikato
• I might want to put sponsors on there as well, possibly 10-20, but maybe only a few if space is a problem

```html
<!DOCTYPE html>
<html lang="en">
<head>
<meta charset="utf-8">
<title>Tarona Mist Fest 2018 – Event Poster</title>
<link rel="stylesheet" href="https://fonts.googleapis.com/css2?family=Graduate&family=Alfa+Slab+One&family=Roboto+Slab:wght@700;800;900&display=swap">
<style>
  :root {
    --page: #1c1c1e;
    --gold-light: #fff3c8;
    --gold: #d9a44a;
    --gold-deep: #8a5a1e;
    --brown: #3d2f25;
    --brown-dark: #241b15;
    --band: rgba(30, 26, 24, 0.92);
    --ink: #111111;
    --white: #ffffff;
    --red: #e30613;
  }
  * { margin: 0; padding: 0; box-sizing: border-box; }
  html, body { width: 1200px; height: 1200px; overflow: hidden; background: var(--page); }
  .poster {
    position: absolute; left: 240px; top: 90px; width: 720px; height: 1018px; overflow: hidden;
    font-family: "Roboto Slab", serif; font-weight: 800; text-align: center; white-space: nowrap;
  }
  .poster-backdrop {
    position: absolute; inset: 0;
    background:
      radial-gradient(ellipse 45% 60% at 52% 12%, var(--gold-light) 0%, rgba(255,243,200,0) 70%),
      radial-gradient(ellipse 50% 40% at 50% 70%, rgba(255,236,190,.85) 0%, rgba(255,236,190,0) 70%),
      linear-gradient(180deg, #c98f3a 0%, var(--gold) 35%, #a4742e 60%, var(--gold-deep) 100%);
  }
  .outlined {
    font-family: "Alfa Slab One", serif; font-weight: 400; color: var(--brown); line-height: 1;
    text-shadow: 2px 2px 0 #fff, -2px -2px 0 #fff, 2px -2px 0 #fff, -2px 2px 0 #fff, 4px 6px 8px rgba(0,0,0,.45);
  }
  .title-line { position: absolute; left: 0; right: 0; letter-spacing: 1px; }
  .title-top { top: 50px; font-size: 60px; transform: rotate(3deg); }
  .title-bottom { top: 110px; font-size: 90px; transform: rotate(1.5deg); }
  .date-ribbon { position: absolute; left: 20px; top: 194px; width: 690px; height: 120px; }
  .date-text {
    position: absolute; left: 0; right: 0; top: 222px;
    font-family: "Graduate", serif; font-weight: 400; color: var(--white); font-size: 30px; line-height: 1.25;
    transform: rotate(3deg); letter-spacing: 1px;
  }
  .rating {
    position: absolute; left: 0; right: 0; top: 322px;
    font-size: 112px; line-height: 1.05; transform: scaleX(0.84);
  }
  .features {
    position: absolute; left: 0; right: 0; top: 444px; height: 110px; background: var(--band);
    color: var(--white); font-size: 27px; line-height: 1.3; padding-top: 18px;
  }
  .venue {
    position: absolute; left: 0; right: 0; top: 562px; color: var(--ink);
    font-size: 32px; line-height: 1.3; font-weight: 900;
  }
  .invite {
    position: absolute; left: 78px; top: 668px; width: 564px; height: 56px; background: var(--band);
    clip-path: polygon(5% 0, 100% 0, 95% 100%, 0 100%);
    color: var(--white); font-size: 24px; line-height: 56px;
  }
  .tickets {
    position: absolute; left: 0; right: 0; top: 736px; color: var(--ink);
    font-size: 34px; line-height: 1.25; font-weight: 900;
  }
  .tickets .url { font-size: 32px; }
  .today-row { position: absolute; left: 0; right: 0; top: 836px; height: 76px; }
  .today {
    position: absolute; left: 0; right: 0; top: 0;
    font-size: 72px; transform: scaleX(0.85);
  }
  .store-name {
    position: absolute; left: 30px; top: 26px; width: 170px;
    color: var(--ink); font-size: 20px; line-height: 1.1;
  }
  .event-mark { position: absolute; left: 528px; top: 14px; display: flex; align-items: center; gap: 8px; }
  .event-mark .square { width: 22px; height: 22px; background: var(--red); }
  .event-mark .name { color: var(--ink); font-size: 18px; line-height: 1.1; text-align: left; }
  .store-note {
    position: absolute; left: 0; right: 0; top: 910px; height: 108px; background: #0f0d0c;
    color: var(--white); font-size: 23px; line-height: 1.3; padding-top: 20px;
  }
</style>
</head>
<body>
<main class="poster">
  <div class="poster-backdrop" role="img" aria-label="Glowing gold background with digital dot pattern and light rays"></div>

  <h1 class="outlined title-line title-top">TARONA MIST</h1>
  <div class="outlined title-line title-bottom">FEST 2018</div>

  <svg class="date-ribbon" viewBox="0 0 690 120" aria-hidden="true">
    <polygon points="10,68 100,40 130,110 40,112" fill="var(--brown-dark)"/>
    <polygon points="680,22 590,20 570,92 660,70" fill="var(--brown-dark)"/>
    <polygon points="88,24 612,2 600,98 88,118" fill="var(--brown)"/>
  </svg>
  <p class="date-text">SATURDAY, 2ND JUNE<br>2018 12-10PM</p>

  <h2 class="outlined rating">R18 EVENT</h2>

  <p class="features">Vendors, Prizes, Comps, E Juice Awards,<br>Entertainment, Giveaways &amp; More</p>

  <p class="venue">The Corner Alehouse<br>(52 Mulgrave Rd, Kerepuni, Hamilton)</p>

  <p class="invite">Come To Tarona's First Mist Fest</p>

  <p class="tickets">Get Your Tickets from<br><span class="url">www.taronamistfest.co.nz</span></p>

  <div class="today-row">
    <span class="store-name">The Cloud Barn</span>
    <span class="outlined today">TODAY</span>
    <span class="event-mark"><span class="square"></span><span class="name">Tarona<br>Mist Fest</span></span>
  </div>

  <p class="store-note">I want people to know they<br>can buy it from a store as well "The Cloud Barn"</p>
</main>
</body>
</html>
```